Business Card Design for my Real Estate Investing Company

This is for a Real Estate Investing Company that will be serving the Las Vegas Valley. Id like the following slogan included: "Investing in Our Community" I have attached my logo. You will see the color tones I'm interested in..in my logo. I would like the card to be double-sided with a modern, professional look.
Target Market(s)
Homeowners, banks, real estate industry
Industry/Entity Type
Real Estate
Contact Information for Business Card
name: Dale Pruitt
position: Managing Member
address: 4812 Corvane Pkwy ste 207-300
N. Las Vegas, NV 89517
phone: (702) 555-0143
fax: (702) 555-0187
email: OakridgeHousePurchaser@examplemail.com
web: OakridgeHousePurchasers.example
*At the bottom of the card I would like....
We buy houses for cash....no repairs, no commissions, no fees!
Logo Text
OAKRIDGE HOUSE PURCHASERS "Investing in Our Community"
Font styles to use
Other font styles liked:
- Lora
Requirements
Must have
- On the back of the card, i'd like to have my logo large and the following statements:
- Are you considering selling your home? Want a simple, hassle-free transaction? We can help! We buy houses for cash and can close quickly! No need to do any repairs, no realtor commissions, no closing costs.....and no headaches. Let us help you with your real estate needs...!
Nice to have
- multiple colors 2 two tone on front and back

```html
<!DOCTYPE html>
<html lang="en">
<head>
<meta charset="utf-8">
<title>Oakridge House Purchasers – Business Cards</title>
<link rel="stylesheet" href="https://fonts.googleapis.com/css2?family=Lora:wght@400;700&family=Arimo:wght@400&display=swap">
<style>
  :root {
    --page: #e9e7e3;
    --card: #ffffff;
    --blue: #1f6fc4;
    --ink: #1a1a1a;
    --band: #0d0d0d;
    --band-text: #f2f2f2;
    --muted: #444444;
  }
  * { box-sizing: border-box; margin: 0; padding: 0; }
  html, body { width: 1200px; height: 902px; overflow: hidden; background: var(--page); }
  .canvas { position: relative; width: 1200px; height: 902px; }

  .card {
    position: absolute;
    width: 560px; height: 320px;
    background: var(--card);
    box-shadow: 0 6px 18px rgba(0,0,0,.18);
    overflow: hidden;
  }
  .card--promo { left: 70px; top: 70px; }
  .card--contact { left: 570px; top: 512px; }

  .brand { display: flex; align-items: center; gap: 10px; font-family: "Lora", serif; color: var(--ink); }
  .brand__square { width: 18px; height: 18px; background: var(--blue); flex: none; }
  .brand__name { font-weight: 400; font-size: 24px; white-space: nowrap; }

  .card--promo .brand { position: absolute; left: 0; right: 0; top: 118px; justify-content: center; }
  .promo__tagline {
    position: absolute; left: 0; right: 0; bottom: 34px; text-align: center;
    font-family: "Lora", serif; color: var(--blue); font-size: 17px;
  }

  .card--contact .brand { position: absolute; left: 30px; top: 88px; }
  .card--contact .brand__name { font-size: 21px; }

  .person { position: absolute; right: 30px; top: 26px; text-align: right; font-family: "Lora", serif; }
  .person__name { font-size: 19px; font-weight: 700; color: var(--ink); }
  .person__role { font-size: 12px; color: var(--muted); }

  .band {
    position: absolute; left: 0; right: 0; top: 178px; height: 108px;
    background: linear-gradient(180deg, #222 0%, var(--band) 60%);
    border-top: 3px solid var(--blue); border-bottom: 3px solid var(--blue);
    display: flex; justify-content: space-between; padding: 14px 26px;
    font-family: "Arimo", sans-serif; color: var(--band-text); font-size: 12.5px;
  }
  .band__col { display: flex; flex-direction: column; gap: 9px; }
  .contact-item { display: flex; align-items: flex-start; gap: 9px; line-height: 1.3; }
  .contact-item__icon { width: 18px; height: 18px; background: var(--blue); flex: none; display: flex; align-items: center; justify-content: center; }
  .contact-item__icon svg { width: 12px; height: 12px; fill: none; stroke: #fff; stroke-width: 1.6; }
</style>
</head>
<body>
<div class="canvas">

  <section class="card card--promo">
    <div class="brand">
      <span class="brand__square"></span>
      <span class="brand__name">Oakridge House Purchasers</span>
    </div>
    <p class="promo__tagline">We buy houses for cash....no repairs, no commissions, no fees!</p>
  </section>

  <section class="card card--contact">
    <div class="brand">
      <span class="brand__square"></span>
      <span class="brand__name">Oakridge House Purchasers</span>
    </div>

    <div class="person">
      <div class="person__name">Dale Pruitt</div>
      <div class="person__role">Managing Member</div>
    </div>

    <div class="band">
      <div class="band__col">
        <div class="contact-item">
          <span class="contact-item__icon"><svg viewBox="0 0 12 12"><path d="M3 1.5l1.5 2.5-1 1c.6 1.3 1.5 2.2 2.8 2.8l1-1 2.5 1.5-1 2C5 10 2 7 1.5 2.5z"/></svg></span>
          <span>(702) 555-0143</span>
        </div>
        <div class="contact-item">
          <span class="contact-item__icon"><svg viewBox="0 0 12 12"><rect x="3" y="1.5" width="6" height="3"/><rect x="1.5" y="4.5" width="9" height="4"/><rect x="3" y="7.5" width="6" height="3"/></svg></span>
          <span>(702) 555-0187</span>
        </div>
        <div class="contact-item">
          <span class="contact-item__icon"><svg viewBox="0 0 12 12"><rect x="1.5" y="3" width="9" height="6"/><path d="M1.5 3l4.5 3.5L10.5 3"/></svg></span>
          <span>OakridgeHousePurchaser@examplemail.com</span>
        </div>
      </div>
      <div class="band__col">
        <div class="contact-item">
          <span class="contact-item__icon"><svg viewBox="0 0 12 12"><circle cx="6" cy="6" r="4.5"/><path d="M1.5 6h9M6 1.5c-2 2.5-2 6.5 0 9M6 1.5c2 2.5 2 6.5 0 9"/></svg></span>
          <span>OakridgeHousePurchasers.example</span>
        </div>
        <div class="contact-item">
          <span class="contact-item__icon"><svg viewBox="0 0 12 12"><path d="M6 11s-3.5-3.8-3.5-6.2a3.5 3.5 0 0 1 7 0C9.5 7.2 6 11 6 11z"/><circle cx="6" cy="4.8" r="1.2"/></svg></span>
          <span>4812 Corvane Pkwy ste 207-300<br>N. Las Vegas, NV 89517</span>
        </div>
      </div>
    </div>
  </section>

</div>
</body>
</html>
```